Redesign PixelHarbor's Designer Account Home Page

Are a web designer? New to PixelHarbor? This contest is for you!

We want you to redesign PixelHarbor's designer account home page. We're looking for bold and innovative ideas to make this page a useful and fun experience for you and your fellow designers.

Only new registrants this month are eligible to enter this contest and win prizes.

Your task:
* We want you to put your web design skills to the test and re-design the My Account home page ("Overview") on PixelHarbor to make it more functional and engaging for designers on PixelHarbor.
* The page you are redesigning is here: http://www.pixelharbor-example.com/my-profile.
* Your design should allow for the same functionality as the existing page, though you don't need to replicate the same elements (buttons) or the same menu structure.
* Your design must fit with the branding of the site.
* You must provide a brief outline of what changes you made and why when you upload your design
* 1 submission per designer - make it your best work!
* Pls see "Must haves" for requirements.

Deadline:
* Submit before 12:00am 1st September UTC. Pls convert this deadline to your local timezone and take note of the local time and date

Prizes: $1,000 to win
* First prize for the best design is $700
* Second prize is $200
* Third prize is $100

If you started from scratch, how would you design the MyAccount page on PixelHarbor?

Good luck & have fun!

Mel / The PixelHarbor Team

Target Market(s)

PixelHarbor designers

Number of Pages Required

1 page

Requirements
Must have
• Dimensions: 1200 x 1000 px
• Minimum 150-300 dpi
• Your design must adhere to our quality standards to be eligible to receive a prize
• Submissions must be created in Adobe Creative Suite (Illustrator or Photoshop)
• Your design must fit with the branding of the PixelHarbor site.
• Only new registrants this month are eligible to enter and win prizes.

```html
<!DOCTYPE html>
<html lang="en">
<head>
<meta charset="utf-8">
<title>PixelHarbor – My Account Overview</title>
<link href="https://fonts.googleapis.com/css2?family=Open+Sans:wght@300;400;600;700&display=swap" rel="stylesheet">
<style>
:root{
  --page:#efefef;
  --card:#ffffff;
  --line:#dcdcdc;
  --ink:#333333;
  --muted:#8a8a8a;
  --blue:#1e73be;
  --blue-soft:#e6f0f9;
  --green:#7ab929;
  --green-dark:#5f9a17;
  --red:#d9352b;
  --track:#e3e3e3;
  --footer:#2c2c2c;
  --footer-deep:#1f1f1f;
  --footer-text:#9a9a9a;
}
*{box-sizing:border-box;margin:0;padding:0}
html,body{width:1200px;height:2212px;overflow:hidden}
body{background:var(--page);font-family:"Open Sans",Arial,sans-serif;color:var(--ink);position:relative;font-size:14px}
.abs{position:absolute}

/* header */
.site-header{left:0;top:0;width:1200px;height:44px;background:var(--card);border-bottom:1px solid var(--line);display:flex;align-items:center;padding:0 56px}
.brand{display:flex;align-items:center;gap:8px;font-weight:700;font-size:20px;color:var(--blue);margin-right:26px}
.brand-mark{width:18px;height:18px;background:var(--blue);border-radius:3px}
.main-nav{display:flex;gap:20px;font-size:12px;color:#555}
.phone{margin-left:22px;font-size:12px;color:#555}
.account-tools{margin-left:auto;display:flex;gap:12px;align-items:center}
.profile-select{border:1px solid var(--line);padding:5px 26px 5px 10px;font-size:12px;border-radius:3px}
.btn-green{background:var(--green);color:#fff;font-weight:600;font-size:12px;padding:6px 14px;border-radius:3px}

.breadcrumb{left:0;top:44px;width:1200px;height:34px;background:#e4e4e4;border-bottom:1px solid var(--line);display:flex;align-items:center;gap:18px;padding:0 56px;font-size:12px;color:#666}
.breadcrumb .home{display:flex;align-items:center;gap:6px}

.page-title{left:0;top:118px;width:1200px;text-align:center;font-size:34px;font-weight:600;color:#3b3b3b}

/* sidebar */
.side{left:56px;top:208px;width:256px}
.browse-btn{background:var(--green);color:#fff;font-size:24px;font-weight:600;height:58px;display:flex;align-items:center;justify-content:space-between;padding:0 18px;border-radius:3px}
.browse-btn .arrow{width:24px;height:24px;border-radius:50%;background:#fff;color:var(--green);font-size:16px;display:flex;align-items:center;justify-content:center}
.side-menu{margin-top:16px;background:var(--card);border:1px solid var(--line)}
.side-menu li{list-style:none;height:44px;border-bottom:1px solid #ececec;display:flex;align-items:center;padding:0 14px;font-size:13px;color:#555;gap:10px}
.side-menu li:last-child{border-bottom:none}
.side-menu li .ico{width:12px;height:12px;border:1.5px solid #aaa;border-radius:2px}
.side-menu li .chev{margin-left:auto;color:#bbb}
.side-menu li.active{background:var(--blue);color:#fff}
.side-menu li.active .ico{border-color:#fff}

/* cards */
.card{background:var(--card);border:1px solid var(--line)}
.stats{left:336px;top:216px;width:808px;height:152px;display:flex;align-items:center;padding:0 22px}
.avatar{width:88px;height:88px;border:1px solid var(--line);display:flex;align-items:center;justify-content:center;margin-right:20px}
.stat{flex:1;text-align:center;border-left:1px solid #ececec;padding:8px 0}
.stat .label{font-size:18px;color:var(--blue);font-weight:600}
.stat .value{font-size:20px;color:#555;margin-top:4px}
.stat .sub{font-size:11px;color:var(--muted);margin-top:4px}
.stars{color:var(--green);font-size:16px;letter-spacing:2px}

.getting{left:336px;top:392px;width:808px;height:672px;padding:30px 34px}
.getting h2{font-size:44px;font-weight:600;color:#444;line-height:1}
.getting .subhead{font-size:30px;font-weight:300;color:#555;margin-top:8px}
.percent{font-size:74px;font-weight:300;color:var(--blue);margin-top:22px;line-height:1}
.percent-label{font-size:16px;color:var(--muted);margin-top:4px}
.donut{right:40px;top:26px}
.todo-title{margin-top:46px;font-size:34px;font-weight:600;color:#444;border-top:1px solid #ececec;padding-top:14px}
.todo{margin-top:12px}
.todo li{list-style:none;height:42px;border-bottom:1px solid #ececec;display:flex;align-items:center;gap:14px;font-size:14px;color:#555}
.todo li .bullet{width:6px;height:6px;background:#999;border-radius:50%}
.todo li.done{font-weight:700;color:#333}
.todo li .state{margin-left:auto;font-size:13px;color:var(--red);font-weight:600}
.todo li .check{margin-left:auto;width:18px;height:18px;border:1.5px solid var(--blue);border-radius:3px}

.jobs{left:336px;top:1088px;width:808px;height:392px;padding:26px 34px}
.section-title{font-size:34px;font-weight:600;color:#444;line-height:1.3}
.section-sub{font-size:13px;color:var(--muted);margin-top:2px}
.job-grid{display:grid;grid-template-columns:1fr 1fr;gap:16px 24px;margin-top:18px}
.job{display:flex;gap:14px;border:1px solid #e6e6e6;padding:12px}
.job-icon{width:58px;height:58px;border-radius:50%;background:var(--blue-soft);border:2px solid var(--blue);flex:none}
.job-title{font-size:18px;color:#444;font-weight:600}
.job-meta{display:grid;grid-template-columns:repeat(4,1fr);gap:6px;margin-top:10px}
.job-meta span{font-size:11px;color:#666;border:1px solid #e6e6e6;text-align:center;padding:3px 0}
.pager{display:flex;justify-content:space-between;margin-top:20px;font-size:12px;color:var(--muted)}
.pager .next{color:var(--blue)}

.achieve{left:336px;top:1504px;width:808px;height:250px;padding:24px 34px}
.ach-grid{display:grid;grid-template-columns:1fr 1fr;gap:12px 24px;margin-top:16px}
.ach{display:flex;gap:12px;align-items:center;border:1px solid #e6e6e6;padding:6px 10px}
.ach-icon{width:34px;height:34px;border-radius:50%;background:var(--blue);flex:none}
.ach-name{font-size:14px;font-weight:600;color:var(--blue)}
.ach-desc{font-size:11px;color:var(--muted)}

/* footer */
.site-footer{left:0;top:1808px;width:1200px;height:352px;background:var(--footer);padding:40px 56px;display:flex;gap:40px}
.f-col h4{color:#fff;font-size:18px;font-weight:600;margin-bottom:16px}
.f-col li{list-style:none;font-size:12px;color:var(--footer-text);line-height:24px}
.f-links{width:140px}
.f-popular{width:250px}
.tags{display:flex;flex-wrap:wrap;gap:6px}
.tags span{border:1px solid #555;color:var(--footer-text);font-size:11px;padding:3px 7px}
.f-news{margin-left:auto;width:260px}
.f-news .row{display:flex;margin-bottom:18px}
.f-news .input{flex:1;height:30px;background:#444}
.f-news .go{width:30px;height:30px;background:var(--green)}
.socials{display:flex;gap:10px;margin-bottom:18px}
.socials span{width:32px;height:32px;border-radius:4px}
.pay{display:flex;gap:6px;margin-bottom:12px}
.pay span{width:36px;height:22px;background:#555;border-radius:2px}
.flags{display:flex;gap:6px;margin-bottom:12px}
.flags span{width:24px;height:16px;background:#666}
.f-brand{display:flex;align-items:center;gap:8px;color:#ddd;font-weight:700;font-size:16px}
.f-brand i{width:14px;height:14px;background:#ddd;border-radius:3px;display:block}
.footer-bar{left:0;top:2160px;width:1200px;height:52px;background:var(--footer-deep);display:flex;align-items:center;justify-content:center;font-size:11px;color:#777}
</style>
</head>
<body>

<header class="site-header abs">
  <div class="brand"><span class="brand-mark"></span>PixelHarbor</div>
  <nav class="main-nav"><span>Categories</span><span>Designers</span><span>Browse Jobs</span><span>How it works</span></nav>
  <span class="phone">1800 555 012</span>
  <div class="account-tools">
    <span class="profile-select">My Profile ▾</span>
    <span class="btn-green">Browse Jobs</span>
  </div>
</header>

<div class="breadcrumb abs"><span class="home">⌂ Home</span><span>›&nbsp; My Profile</span></div>

<h1 class="page-title abs">Overview</h1>

<aside class="side abs">
  <div class="browse-btn">Browse Jobs <span class="arrow">›</span></div>
  <ul class="side-menu">
    <li class="active"><span class="ico"></span>Overview<span class="chev">›</span></li>
    <li><span class="ico"></span>Contests<span class="chev">›</span></li>
    <li><span class="ico"></span>Profile<span class="chev">›</span></li>
    <li><span class="ico"></span>Submissions<span class="chev">›</span></li>
    <li><span class="ico"></span>Messages<span class="chev">›</span></li>
    <li><span class="ico"></span>Watchlist<span class="chev">›</span></li>
    <li><span class="ico"></span>Widgets<span class="chev">›</span></li>
    <li><span class="ico"></span>My Profile<span class="chev">›</span></li>
  </ul>
</aside>

<section class="stats card abs">
  <div class="avatar">
    <svg width="56" height="56" viewBox="0 0 56 56"><circle cx="28" cy="20" r="11" fill="var(--blue)"/><path d="M6 54c2-14 12-20 22-20s20 6 22 20z" fill="var(--blue)"/></svg>
  </div>
  <div class="stat"><div class="label">Rank</div><div class="value">#56577</div><div class="sub">of 47,412 designers</div></div>
  <div class="stat"><div class="label">Positive</div><div class="stars">★★★★★</div><div class="sub">40%</div></div>
  <div class="stat"><div class="label">Submissions</div><div class="value">112</div><div class="sub">last average: 7</div></div>
  <div class="stat"><div class="label">Earnings</div><div class="value">$1200.00</div><div class="sub">last average: $1200.00</div></div>
</section>

<section class="getting card abs">
  <h2>Getting Started</h2>
  <div class="subhead">Complete Your Profile</div>
  <div class="percent">72 %</div>
  <div class="percent-label">Complete</div>
  <svg class="donut abs" width="260" height="260" viewBox="0 0 260 260" aria-hidden="true">
    <circle cx="130" cy="130" r="100" fill="none" stroke="var(--track)" stroke-width="40"/>
    <circle cx="130" cy="130" r="100" fill="none" stroke="var(--blue)" stroke-width="40" stroke-dasharray="452.4 628.3" transform="rotate(-90 130 130)"/>
  </svg>
  <div class="todo-title">Things left to do:</div>
  <ul class="todo">
    <li><span class="bullet"></span>Tell us what type of designer you are<span class="check"></span></li>
    <li class="done"><span class="bullet"></span>Verify your payment address<span class="state">Complete</span></li>
    <li><span class="bullet"></span>Visit the Jobs Board<span class="check"></span></li>
    <li class="done"><span class="bullet"></span>Add your profile pic<span class="state">Complete</span></li>
    <li><span class="bullet"></span>Add an about me to your profile<span class="check"></span></li>
    <li><span class="bullet"></span>Review and accept the PixelHarbor quality standards<span class="check"></span></li>
    <li><span class="bullet"></span>Submit your first designs<span class="check"></span></li>
  </ul>
</section>

<section class="jobs card abs">
  <h2 class="section-title">Recommended Jobs</h2>
  <p class="section-sub">There is over $23813 waiting for you on these jobs that don't have any submissions yet.</p>
  <div class="job-grid">
    <div class="job"><span class="job-icon"></span><div><div class="job-title">Sealing Company Logo Design</div><div class="job-meta"><span>5 days left</span><span>0 entries</span><span>$ 250</span><span>Watchlist</span></div></div></div>
    <div class="job"><span class="job-icon"></span><div><div class="job-title">Sealing Company Logo Design</div><div class="job-meta"><span>5 days left</span><span>0 entries</span><span>$ 250</span><span>Watchlist</span></div></div></div>
    <div class="job"><span class="job-icon"></span><div><div class="job-title">Sealing Company Logo Design</div><div class="job-meta"><span>5 days left</span><span>0 entries</span><span>$ 250</span><span>Watchlist</span></div></div></div>
    <div class="job"><span class="job-icon"></span><div><div class="job-title">Sealing Company Logo Design</div><div class="job-meta"><span>5 days left</span><span>0 entries</span><span>$ 250</span><span>Watchlist</span></div></div></div>
  </div>
  <div class="pager"><span>Page 1</span><span>‹ Prev &nbsp; <span class="next">Next ›</span></span></div>
</section>

<section class="achieve card abs">
  <h2 class="section-title">Achievements</h2>
  <p class="section-sub">Earn designer level achievements as you unlock milestones.</p>
  <div class="ach-grid">
    <div class="ach"><span class="ach-icon"></span><div><div class="ach-name">True designer(Next)</div><div class="ach-desc">Submit at least 1000 design to contests</div></div></div>
    <div class="ach"><span class="ach-icon"></span><div><div class="ach-name">True designer(Next)</div><div class="ach-desc">Submit at least 1000 design to contests</div></div></div>
    <div class="ach"><span class="ach-icon"></span><div><div class="ach-name">Cha-ching (Next)</div><div class="ach-desc">Earn at least $20000 in earnings</div></div></div>
    <div class="ach"><span class="ach-icon"></span><div><div class="ach-name">Cha-ching (Next)</div><div class="ach-desc">Earn at least $20000 in earnings</div></div></div>
  </div>
</section>

<footer class="site-footer abs">
  <div class="f-col f-links"><h4>I need a...</h4><ul><li>Logo Design</li><li>Website Design</li><li>Business Cards</li><li>Brochure Design</li><li>Banner Ads</li><li>T-Shirt Design</li><li>Label Design</li><li>Illustration</li></ul></div>
  <div class="f-col f-links"><h4>Find a...</h4><ul><li>Logo Designer</li><li>Web Designer</li><li>Graphic Designer</li><li>Print Designer</li><li>Freelancer</li><li>Illustrator</li><li>Copywriter</li></ul></div>
  <div class="f-col f-links"><h4>About us</h4><ul><li>About</li><li>Careers</li><li>Press</li><li>Blog</li><li>Contact</li><li>Privacy</li><li>Terms</li></ul></div>
  <div class="f-col f-popular"><h4>Popular pages</h4><div class="tags"><span>Logo Contests</span><span>Web Design</span><span>Poster Design</span><span>Flyers</span><span>Business Cards</span><span>Packaging</span><span>Apps</span><span>Icons</span><span>Banners</span></div></div>
  <div class="f-col f-news">
    <h4 style="font-size:13px">Subscribe to our newsletter</h4>
    <div class="row"><span class="input"></span><span class="go"></span></div>
    <div class="socials"><span style="background:#3b5998"></span><span style="background:#55acee"></span><span style="background:#dd4b39"></span><span style="background:#cb2027"></span><span style="background:#0e76a8"></span></div>
    <div class="pay"><span></span><span></span><span></span><span></span></div>
    <div class="flags"><span></span><span></span><span></span><span></span><span></span></div>
    <div class="f-brand"><i></i>PixelHarbor</div>
  </div>
</footer>
<div class="footer-bar abs">Copyright © 2013 PixelHarbor. All rights reserved. Terms of use and privacy policy.</div>

</body>
</html>
```